Brackenford Solar Project Sign - 36" x 48" color poster

Need a 36" x 48" sign to put next to our solar project. The solar project is installed and we will print this sign on plastic corrugated board and mount as an informational kiosk next to the project. A picture of a similar kiosk is attached. Its is important that the information is easy to understand and aesthetically pleasing. I've uploaded a draft that we did with the information and general idea. The draft is not the correct dimensions and will not scale to the appropriate size. Looking for a professional to do this well. Thank you !!
Target Market(s)
teenage school children and their parents.
Industry/Entity Type
Solar Energy
Requirements
Must have
- technical information included in the draft. Must include the photo of the solar project. Must include the Tallow Brook Solar Logo. Must be scaled to 36" x 48".
Nice to have
- Color scheme that complements the tallow brook solar logo colors
Should not have
- stock photos

```html
<!DOCTYPE html>
<html lang="en">
<head>
<meta charset="utf-8">
<title>Brackenford School District Solar</title>
<link rel="stylesheet" href="https://fonts.googleapis.com/css2?family=Open+Sans:wght@400;700;800&family=Source+Sans+3:wght@400;600;700&display=swap">
<style>
  :root {
    --page: #e4e4e4;
    --orange: #f29a2e;
    --amber: #e9b52a;
    --lime: #a9cf3a;
    --leaf: #8cc63f;
    --grass: #9fd23b;
    --sky-blue: #2f6db5;
    --badge-blue: #35a8dc;
    --cream: #fff4b8;
    --white: #ffffff;
    --ink: #333333;
    --logo-green: #4a9a3a;
  }
  * { box-sizing: border-box; margin: 0; padding: 0; }
  html, body { width: 1200px; height: 1200px; overflow: hidden; }
  body { background: var(--page); position: relative; font-family: "Source Sans 3", sans-serif; }

  .poster {
    position: absolute; left: 179px; top: 40px;
    width: 791px; height: 1053px;
    transform: scale(1.0636); transform-origin: top left;
    overflow: hidden;
    background:
      radial-gradient(ellipse 70% 45% at 25% 30%, rgba(242,140,40,.95), rgba(242,140,40,0) 70%),
      linear-gradient(160deg, #e6c42a 0%, var(--lime) 45%, var(--grass) 100%);
  }

  .title { position: absolute; left: 0; right: 0; text-align: center; color: var(--white);
    font-family: "Open Sans", sans-serif; font-weight: 800; line-height: 1;
    text-shadow: 0 3px 6px rgba(0,0,0,.25); }
  .title-line { font-size: 66px; letter-spacing: -0.5px; }
  .title-town { top: 40px; }
  .title-district { top: 118px; }
  .title-solar { top: 180px; font-size: 182px; letter-spacing: -4px; }

  .site-photo { position: absolute; left: 0; top: 368px; width: 791px; height: 420px;
    background: linear-gradient(180deg, rgba(255,236,200,0) 0%, #8c7fb0 14%, #5a5aa0 28%, #3d5cc0 38%, #c9a98a 50%, #c8b486 70%, rgba(190,200,90,.6) 88%, rgba(190,200,90,0) 100%); }

  .incentives { position: absolute; left: 44px; top: 552px; width: 470px;
    color: var(--sky-blue); font-weight: 700; font-size: 25px; line-height: 33px; white-space: nowrap; }

  .diagram-card, .chart-card { position: absolute; left: 572px; width: 164px; z-index: 2;
    background: var(--white); box-shadow: 0 2px 6px rgba(0,0,0,.3); }
  .diagram-card { top: 572px; height: 103px; }
  .panel-layers { position: absolute; inset: 6px; background: linear-gradient(160deg, #dfe6f2, #4a63b8 55%, #e8ecf2); }
  .chart-card { top: 692px; height: 98px; }

  .facts-band { position: absolute; left: 0; top: 795px; width: 791px; height: 185px;
    background: linear-gradient(180deg, #d6b52a 0%, var(--amber) 45%, var(--orange) 100%); }

  .badge { position: absolute; left: 21px; top: 823px; width: 120px; height: 120px; }
  .badge-text { position: absolute; left: 21px; top: 838px; width: 120px; text-align: center; color: var(--white); font-size: 14px; line-height: 18px; }
  .badge-year { display: block; font-family: "Open Sans", sans-serif; font-weight: 800; font-size: 30px; line-height: 28px; }

  .facts { position: absolute; left: 166px; top: 818px; width: 570px; display: grid;
    grid-template-columns: 292px 278px; list-style: none; }
  .fact { position: relative; padding: 3px 0 6px 18px; color: var(--cream);
    font-weight: 700; font-size: 17px; line-height: 19px; text-transform: uppercase; list-style: none; }
  .fact::before { content: ""; position: absolute; left: 0; top: 8px; width: 9px; height: 9px; border-radius: 50%; background: #f6d743; }
  .fact:nth-child(odd) { border-right: 1px solid rgba(255,244,184,.5); }
  .fact:nth-child(3), .fact:nth-child(4) { border-top: 1px solid rgba(255,244,184,.5); padding-top: 20px; }
  .fact:nth-child(3)::before, .fact:nth-child(4)::before { top: 25px; }
  .fact:nth-child(even) { padding-left: 34px; }
  .fact:nth-child(even)::before { left: 16px; }

  .footer-band { position: absolute; left: 0; top: 978px; width: 791px; height: 75px; background: var(--grass); }
  .footer-wing { position: absolute; top: 953px; }
  .brand-box { position: absolute; left: 212px; top: 953px; width: 367px; height: 77px;
    background: var(--white); display: flex; align-items: center; justify-content: center; }
  .brand-name { font-family: "Open Sans", sans-serif; font-weight: 800; font-size: 27px; white-space: nowrap;
    color: var(--logo-green); letter-spacing: .3px; text-transform: uppercase; }
  .partner-mark { position: absolute; left: 652px; top: 977px; width: 54px; height: 54px; background: var(--white); }
  .partner-mark span { position: absolute; inset: 6px; border-radius: 50%; background: #cfcfcf; }
</style>
</head>
<body>
  <main class="poster">
    <h1 class="title title-line title-town">BRACKENFORD</h1>
    <div class="title title-line title-district">SCHOOL DISTRICT</div>
    <div class="title title-solar">SOLAR</div>

    <div class="site-photo" role="img" aria-label="Photo of the ground-mounted solar array in a field in front of a tree line"></div>

    <div class="facts-band"></div>

    <p class="incentives">Incentives from Vermont’s<br>net metering program,<br>renewable energy credits and<br>energy savings pay for this project<br>without adding cost to<br>the district or tax payers</p>

    <div class="diagram-card"><div class="panel-layers" role="img" aria-label="Exploded diagram of solar panel layers"></div></div>

    <div class="chart-card">
      <svg width="164" height="98" viewBox="0 0 164 98" aria-label="Monthly expected energy chart">
        <line x1="18" y1="8" x2="18" y2="68" stroke="#999" stroke-width=".6"/>
        <line x1="18" y1="68" x2="146" y2="68" stroke="#999" stroke-width=".6"/>
        <g fill="#2f5fc0">
          <rect x="22" y="42" width="4" height="26"/><rect x="32" y="38" width="4" height="30"/>
          <rect x="42" y="34" width="4" height="34"/><rect x="52" y="30" width="4" height="38"/>
          <rect x="62" y="24" width="4" height="44"/><rect x="72" y="20" width="4" height="48"/>
          <rect x="82" y="18" width="4" height="50"/><rect x="92" y="12" width="4" height="56"/>
          <rect x="102" y="22" width="4" height="46"/><rect x="112" y="36" width="4" height="32"/>
          <rect x="122" y="46" width="4" height="22"/><rect x="132" y="50" width="4" height="18"/>
        </g>
        <polyline fill="none" stroke="#f2b33a" stroke-width="1" points="24,44 34,38 44,32 54,26 64,20 74,24 84,20 94,10 104,26 114,40 124,48 134,54"/>
        <g font-size="5" fill="#555" font-family="Source Sans 3, sans-serif" text-anchor="middle">
          <text x="24" y="76">J</text><text x="34" y="76">F</text><text x="44" y="76">M</text><text x="54" y="76">A</text>
          <text x="64" y="76">M</text><text x="74" y="76">J</text><text x="84" y="76">J</text><text x="94" y="76">A</text>
          <text x="104" y="76">S</text><text x="114" y="76">O</text><text x="124" y="76">N</text><text x="134" y="76">D</text>
          <rect x="34" y="88" width="8" height="2" fill="#2f5fc0"/><text x="58" y="91">Expected Energy</text>
          <rect x="90" y="88" width="8" height="1" fill="#f2b33a"/><text x="112" y="91">Irradiance</text>
        </g>
      </svg>
    </div>

    <svg class="badge" viewBox="0 0 120 120" aria-hidden="true">
      <polygon fill="var(--badge-blue)" stroke="#ffffff" stroke-width="1.5" points="60,2 68,14 82,6 84,22 100,20 96,36 112,40 102,52 116,62 102,72 110,86 94,88 96,104 80,100 72,114 60,104 48,114 40,100 24,104 26,88 10,86 18,72 4,62 18,52 8,40 24,36 20,20 36,22 38,6 52,14"/>
    </svg>
    <div class="badge-text">Project<br>Completed<br>December<span class="badge-year">2015</span></div>

    <ul class="facts">
      <li class="fact">Project provides energy savings to school district</li>
      <li class="fact">Provides curriculum opportunity for students</li>
      <li class="fact">New powerline provides electricity to snack shack</li>
      <li class="fact">Solar energy generated without burning fossil</li>
    </ul>

    <div class="footer-band"></div>
    <svg class="footer-wing" style="left:198px" width="16" height="26" aria-hidden="true"><polygon points="16,0 16,26 0,26" fill="#2f6db5"/></svg>
    <svg class="footer-wing" style="left:577px" width="16" height="26" aria-hidden="true"><polygon points="0,0 16,26 0,26" fill="#2f6db5"/></svg>
    <div class="brand-box"><span class="brand-name">Tallow Brook Solar</span></div>
    <div class="partner-mark" aria-label="Partner badge"><span></span></div>
  </main>
</body>
</html>
```